Bubble map/flip book

I need someone to create a bubble map with explanations using the attached. This will be used to create a color coded flip book/manual. I need you to clean this up.

Mirandalowsky@plinkmail.com

```html
<!DOCTYPE html>
<html lang="en">
<head>
<meta charset="utf-8">
<title>Denied Claims Flip Book</title>
<link href="https://fonts.googleapis.com/css2?family=Open+Sans:ital,wght@0,400;0,600;0,700;1,400&display=swap" rel="stylesheet">
<style>
:root{
  --stage:#9b9b9b;
  --ink:#222;
  --black:#1e1e1e;
  --yellow:#f9d000;
  --pink:#e8196f;
  --green:#3f7a2b;
  --brown:#8d6116;
  --violet:#4a2a8f;
  --blue:#0c56a6;
  --orange:#f38a1f;
}
*{box-sizing:border-box;margin:0;padding:0}
html,body{width:1008px;height:1200px;overflow:hidden}
body{background:var(--stage);font-family:"Open Sans",Arial,sans-serif;color:var(--ink);position:relative}
.page{position:absolute;width:222px;height:282px;background:linear-gradient(150deg,#fff 0%,#f6f6f6 45%,#ececec 100%);overflow:hidden}
.page.yellow{--c:var(--yellow)}.page.pink{--c:var(--pink)}.page.green{--c:var(--green)}
.page.brown{--c:var(--brown)}.page.violet{--c:var(--violet)}.page.blue{--c:var(--blue)}
.page.orange{--c:var(--orange)}.page.black{--c:var(--black)}
.wires{position:absolute;left:0;top:0;width:222px;height:282px}
.corner{position:absolute;right:0;bottom:0;width:28px;height:28px}
.banner{position:absolute;left:14px;width:189px;background:var(--c);color:#fff;font-weight:700;font-size:7px;display:flex;align-items:center;justify-content:center;text-align:center;line-height:1.25;text-transform:uppercase;box-shadow:0 1.5px 0 rgba(0,0,0,.35)}
.page.yellow .banner{color:#111}
.box{position:absolute;background:var(--c);color:#fff;font-size:3.8px;line-height:1.3;display:flex;flex-direction:column;align-items:center;justify-content:center;text-align:center;padding:2px 3px}
.page.yellow .box{color:#333}
.box em{font-style:italic}
.box.lead{font-size:5.5px}
.box.lead em{font-size:3.6px}
.tile{position:absolute;color:#fff;font-size:5.6px;line-height:1.2;display:flex;align-items:center;justify-content:center;text-align:center;padding:2px}
.dot{position:absolute;width:4px;height:4px;border-radius:50%;top:51px}
.heading{position:absolute;left:20px;width:182px;text-align:center;font-weight:700;font-size:6.6px;color:var(--c);text-transform:uppercase;line-height:1.3}
.page.yellow .heading{color:#e9b400}
.rule{position:absolute;left:20px;width:182px;height:2.5px;background:var(--c)}
.copy{position:absolute;font-size:3.5px;line-height:1.35;color:#333}
.copy p{margin-bottom:2.5px}
.copy b{font-weight:700}
.copy ul{list-style:none;margin-bottom:2.5px}
.copy .sub{color:var(--c);font-weight:700;font-size:3.8px}
.side{position:absolute;font-size:3.6px;line-height:1.4;color:var(--blue)}
</style>
</head>
<body>
<svg width="0" height="0" style="position:absolute">
  <defs>
    <marker id="ah-yellow" viewBox="0 0 6 6" refX="5" refY="3" markerWidth="4" markerHeight="4" orient="auto"><path d="M0 0L6 3L0 6z" fill="#f1a81c"/></marker>
    <marker id="ah-pink" viewBox="0 0 6 6" refX="5" refY="3" markerWidth="4" markerHeight="4" orient="auto"><path d="M0 0L6 3L0 6z" fill="#e8196f"/></marker>
    <marker id="ah-green" viewBox="0 0 6 6" refX="5" refY="3" markerWidth="4" markerHeight="4" orient="auto"><path d="M0 0L6 3L0 6z" fill="#3f7a2b"/></marker>
    <marker id="ah-brown" viewBox="0 0 6 6" refX="5" refY="3" markerWidth="4" markerHeight="4" orient="auto"><path d="M0 0L6 3L0 6z" fill="#8d6116"/></marker>
    <marker id="ah-violet" viewBox="0 0 6 6" refX="5" refY="3" markerWidth="4" markerHeight="4" orient="auto"><path d="M0 0L6 3L0 6z" fill="#4a2a8f"/></marker>
    <marker id="ah-blue" viewBox="0 0 6 6" refX="5" refY="3" markerWidth="4" markerHeight="4" orient="auto"><path d="M0 0L6 3L0 6z" fill="#0c56a6"/></marker>
    <marker id="ah-orange" viewBox="0 0 6 6" refX="5" refY="3" markerWidth="4" markerHeight="4" orient="auto"><path d="M0 0L6 3L0 6z" fill="#f38a1f"/></marker>
  </defs>
</svg>

<!-- Row 1 -->
<section class="page black" style="left:58px;top:26px">
  <svg class="wires" viewBox="0 0 222 282" fill="none" stroke-width=".7">
    <path d="M30 53V134" stroke="#f9d000"/><path d="M56 53V187" stroke="#e8196f"/>
    <path d="M82 53V134" stroke="#3f7a2b"/><path d="M110 53V187" stroke="#8d6116"/>
    <path d="M135 53V134" stroke="#4a2a8f"/><path d="M163 53V187" stroke="#0c56a6"/>
    <path d="M189 53V134" stroke="#f38a1f"/>
  </svg>
  <div class="banner" style="top:22px;height:31px;font-size:11.5px;font-weight:600">Claim Has Been Denied</div>
  <span class="dot" style="left:28px;background:var(--yellow)"></span><span class="dot" style="left:54px;background:var(--pink)"></span>
  <span class="dot" style="left:80px;background:var(--green)"></span><span class="dot" style="left:108px;background:var(--brown)"></span>
  <span class="dot" style="left:133px;background:var(--violet)"></span><span class="dot" style="left:161px;background:var(--blue)"></span>
  <span class="dot" style="left:187px;background:var(--orange)"></span>
  <div class="tile" style="left:10px;top:134px;width:40px;height:40px;background:var(--yellow)">Authorization/ Referral Needed</div>
  <div class="tile" style="left:63px;top:134px;width:39px;height:40px;background:var(--green)">Duplicate</div>
  <div class="tile" style="left:115px;top:134px;width:39px;height:40px;background:var(--violet)">Global Inclusive</div>
  <div class="tile" style="left:170px;top:134px;width:39px;height:40px;background:var(--orange)">Past Timely Filing</div>
  <div class="tile" style="left:36px;top:187px;width:41px;height:41px;background:var(--pink)">Coding/ Billing Issues</div>
  <div class="tile" style="left:90px;top:187px;width:40px;height:41px;background:var(--brown)">Non-Covered Charge</div>
  <div class="tile" style="left:143px;top:187px;width:40px;height:41px;background:var(--blue)">Additional Information Requested</div>
  <svg class="corner" viewBox="0 0 28 28"><path d="M28 0V28H0z" fill="#555"/><path d="M28 9V28H9z" fill="#1e1e1e"/></svg>
</section>

<section class="page yellow" style="left:283px;top:26px">
  <svg class="wires" viewBox="0 0 222 282" fill="none" stroke="#f1a81c" stroke-width=".6">
    <path d="M108 90V98M51 98H168"/><path d="M51 98V109" marker-end="url(#ah-yellow)"/><path d="M168 98V109" marker-end="url(#ah-yellow)"/>
    <path d="M27 155V181" marker-end="url(#ah-yellow)"/><path d="M77 155V181" marker-end="url(#ah-yellow)"/>
    <path d="M141 155V181" marker-end="url(#ah-yellow)"/><path d="M192 155V181" marker-end="url(#ah-yellow)"/>
  </svg>
  <div class="banner" style="top:22px;height:32px">Claim denied for no authorization/referral.</div>
  <div class="box lead" style="left:58px;top:64px;width:101px;height:26px">Contact carrier.<em>Was claim processed in network or out of network?</em></div>
  <div class="box" style="left:17px;top:110px;width:68px;height:45px">Claim processed correctly as in network provider. Medical records printed and sent for medical necessity.</div>
  <div class="box" style="left:134px;top:110px;width:67px;height:45px">Claim processed out of network. Contact with carrier shows claim processed as out of network in error.<em>Will representative send the claim back for review?</em></div>
  <div class="box" style="left:12px;top:182px;width:30px;height:48px">Appeal denied as services were not emergent. Balance is patient responsibility</div>
  <div class="box" style="left:62px;top:182px;width:31px;height:48px">Appeal for claim paid.</div>
  <div class="box" style="left:126px;top:182px;width:31px;height:48px">Claim has been sent back for review. Follow up in 14 days.</div>
  <div class="box" style="left:177px;top:182px;width:30px;height:48px">Representative will not send the claim back for review. Appeal sent to carrier. Follow up in 30 days.</div>
  <svg class="corner" viewBox="0 0 28 28"><path d="M28 0V28H0z" fill="#fbe580"/><path d="M28 9V28H9z" fill="#f9d000"/></svg>
</section>

<section class="page yellow" style="left:508px;top:26px">
  <div class="heading" style="top:24px">Authorization/Referral Needed.</div>
  <div class="rule" style="top:33px"></div>
  <div class="copy" style="left:40px;top:50px;width:140px">
    <p>1. If you are a network provider verify that the claim processed correctly in network. If claim processed out of network have the claim sent back to process and send appeal stating that claim processed incorrectly out of network.</p>
    <p>2. If you are not a network provider you may send an appeal with medical records attached stating to reprocess and pay claim based on medical necessity.</p>
    <p><b>NOTES ON ACCOUNT SHOULD INCLUDE:</b></p>
    <ul><li>- Claim number</li><li>- Denial date</li><li>- Processed in or out of network</li></ul>
  </div>
  <svg class="corner" viewBox="0 0 28 28"><path d="M28 0V28H0z" fill="#fbe580"/><path d="M28 9V28H9z" fill="#f9d000"/></svg>
</section>

<section class="page pink" style="left:733px;top:26px">
  <svg class="wires" viewBox="0 0 222 282" fill="none" stroke="#e8196f" stroke-width=".6">
    <path d="M108 91V98M50 98H167"/><path d="M50 98V105" marker-end="url(#ah-pink)"/><path d="M167 98V105" marker-end="url(#ah-pink)"/>
    <path d="M141 157V180" marker-end="url(#ah-pink)"/><path d="M193 157V180" marker-end="url(#ah-pink)"/>
  </svg>
  <div class="banner" style="top:22px;height:32px;font-size:7.6px">Coding Denial<br>CPT/DX/Modifier</div>
  <div class="box lead" style="left:58px;top:62px;width:100px;height:29px;font-size:5px">Contact made with carrier.</div>
  <div class="box" style="left:15px;top:106px;width:70px;height:51px">Claim denied in error and has been sent back to process.</div>
  <div class="box" style="left:132px;top:106px;width:70px;height:51px">Claim denied correctly for coding error</div>
  <div class="box" style="left:126px;top:181px;width:30px;height:49px">Forwarded to physician for review</div>
  <div class="box" style="left:178px;top:181px;width:30px;height:49px">Corrected and rebilled as a corrected claim</div>
  <svg class="corner" viewBox="0 0 28 28"><path d="M28 0V28H0z" fill="#f38cb7"/><path d="M28 9V28H9z" fill="#e8196f"/></svg>
</section>

<!-- Row 2 -->
<section class="page pink" style="left:58px;top:314px">
  <div class="heading" style="top:23px">Coding Denial</div>
  <div class="rule" style="top:33px"></div>
  <div class="copy" style="left:58px;top:50px;width:120px">
    <p><b>Example:</b><br>*Claim denied as procedure code used 99203 is for a new patient and this is an established patient.</p>
    <p><b>ACCOUNT NOTE WILL INCLUDE:</b><br>* How information was obtained<br>* Name of representative<br>* Claim number<br>* Denial date<br>* What was denied: CPT, HCPCS, modifier, diagnosis?<br>* What code denied?<br>* Why was it denied?<br>&nbsp;&nbsp;A. Not covered?<br>&nbsp;&nbsp;B. Bundled to another code on the claim? Which code is bundled with?<br>&nbsp;&nbsp;C. Not a covered benefit per patient policy? Why? What is the service?<br>&nbsp;&nbsp;D. Invalid modifier? What modifier was billed? What is needed?<br>&nbsp;&nbsp;E. Diagnosis does not match CPT? Verify codes billed do not relate to each other.<br>*Appeal address<br>*Timely filing</p>
    <p><b>*Verify that the claim was billed with the CPT code stated.</b></p>
  </div>
  <svg class="corner" viewBox="0 0 28 28"><path d="M28 0V28H0z" fill="#f38cb7"/><path d="M28 9V28H9z" fill="#e8196f"/></svg>
</section>

<section class="page green" style="left:283px;top:314px">
  <svg class="wires" viewBox="0 0 222 282" fill="none" stroke="#3f7a2b" stroke-width=".6">
    <path d="M108 90V100M38 100H168"/><path d="M38 100V109" marker-end="url(#ah-green)"/><path d="M168 100V109" marker-end="url(#ah-green)"/>
    <path d="M38 154V166M27 166H77"/><path d="M27 166V177" marker-end="url(#ah-green)"/><path d="M77 166V177" marker-end="url(#ah-green)"/>
  </svg>
  <div class="banner" style="top:22px;height:29px">Claim Denied as a Duplicate</div>
  <div class="box" style="left:53px;top:66px;width:110px;height:24px;font-size:4.8px">Verify that your office has not sent two claims for this date of service</div>
  <div class="box" style="left:14px;top:110px;width:48px;height:44px">Only 1 claim billed. Contact with carrier shows other claim billed under a different NPI or Tax ID.<em>Will representative send claim back to process?</em></div>
  <div class="box" style="left:133px;top:110px;width:69px;height:44px">Two claims billed. If additional charges were added combine charges and rebill as corrected claim.<br><br>If two identical claims sent in error void claim.</div>
  <div class="box" style="left:11px;top:178px;width:31px;height:52px">Rep. sent claim back to process for payment</div>
  <div class="box" style="left:62px;top:178px;width:31px;height:52px">Rep. will not send claim back to process. Send appeal with medical records</div>
  <svg class="corner" viewBox="0 0 28 28"><path d="M28 0V28H0z" fill="#9bbd8f"/><path d="M28 9V28H9z" fill="#3f7a2b"/></svg>
</section>

<section class="page green" style="left:508px;top:314px">
  <div class="heading" style="top:23px">Duplicate</div>
  <div class="rule" style="top:33px"></div>
  <div class="copy" style="left:25px;top:42px;width:174px;font-size:3.2px">
    <p>Review the record to verify that the service rendered was actually performed and billed just once. If the service has been performed and billed only once, then contacting the insurance company and reviewing the claim with a claims specialist may be the best option.</p>
    <p>Duplicate service denial is indicated when the same service was performed on the same patient on the same date and by the same provider.</p>
    <p><b>Three reasons a claim may be denied as duplicate:</b><br>1. The service was performed more than once on the same day validating the denial.<br>2. The service was performed once but billed twice.<br>3. Another physician performed the same service on the same date and submitted a claim with the same CPT code you did, which was processed prior to your claim.</p>
    <p><b>How to respond to a claim denied as a duplicate:</b><br>1. If the service was performed more than once on the same day it may be eligible for a modifier. Modifier 59 or 91 and 76 or 77 may be appended to indicate the same procedure performed bilaterally and may clear up the confusion. If it was performed more than once during the same day and by the same provider, you may need to append modifier 76 and rebill. If you have already done that and it still denied, simply submit a letter of appeal with a copy of each report for that specific service for proof it was performed more than once and is not a duplicate service.<br>2. If you find you have actually submitted the claim twice then you may need to verify a few things:</p>
    <ul style="padding-left:8px">
      <li>• Was payment made on the first claim and if so, was it sent to the correct address?</li>
      <li>• Has the check been deposited and somehow missed in the posting process?</li>
      <li>• Was the payment sent to the patient for failure to check the accept assignment box on the HCFA form?</li>
      <li>• Was the first claim submitted denied? If denied, was the denial handled correctly? Some insurances will allow you to simply correct a diagnosis code, modifier, or other problem and simply resubmit the claim.</li>
    </ul>
    <p>Some insurances will deny the claim if it is resubmitted with the changes instead of appealed. Be sure you understand the claim resubmission policy for each insurance you are contracted with.</p>
    <p>3. If another provider has performed the same service and was paid while your claim was denied you may need to speak to your insurance representative to determine the proper method of appeal required by the insurance. Methods of appeal may vary by insurance.<br>In short, a denial for duplicate service does not mean the claim will never be paid. Do a little research and see if any of the scenarios above fit your particular situation and then act accordingly.</p>
  </div>
  <svg class="corner" viewBox="0 0 28 28"><path d="M28 0V28H0z" fill="#9bbd8f"/><path d="M28 9V28H9z" fill="#3f7a2b"/></svg>
</section>

<section class="page brown" style="left:733px;top:314px">
  <svg class="wires" viewBox="0 0 222 282" fill="none" stroke="#8d6116" stroke-width=".6">
    <path d="M108 90V101M50 101H168"/><path d="M50 101V107" marker-end="url(#ah-brown)"/><path d="M168 101V107" marker-end="url(#ah-brown)"/>
    <path d="M29 166V191" marker-end="url(#ah-brown)"/><path d="M77 166V191" marker-end="url(#ah-brown)"/>
  </svg>
  <div class="banner" style="top:22px;height:30px">Claim Denied as Non-Covered</div>
  <div class="box lead" style="left:58px;top:64px;width:100px;height:26px;font-size:5px">Contact Carrier.</div>
  <div class="box" style="left:15px;top:108px;width:70px;height:58px">Claim denied correctly.<em>What is non-covered? The diagnosis or CPT Code?<br><br>Is the diagnosis a policy exclusion (Exp - Obesity related Dx)<br>Send back to the physician to see if diagnosis can be changed</em></div>
  <div class="box" style="left:133px;top:108px;width:69px;height:58px">Claim denied in error and claim has been sent back to process</div>
  <div class="box" style="left:15px;top:192px;width:28px;height:38px">Dx updated and claim rebilled as corrected claim</div>
  <div class="box" style="left:62px;top:192px;width:30px;height:38px">Physician unable to change Dx. Appeal with medical records</div>
  <svg class="corner" viewBox="0 0 28 28"><path d="M28 0V28H0z" fill="#c9ad7d"/><path d="M28 9V28H9z" fill="#8d6116"/></svg>
</section>

<!-- Row 3 -->
<section class="page brown" style="left:58px;top:603px">
  <div class="heading" style="top:23px">Non-Covered</div>
  <div class="rule" style="top:33px"></div>
  <div class="copy" style="left:33px;top:46px;width:156px;font-size:3.3px">
    <p>Insurance companies determine what tests, drugs and services they will cover. These choices are based on their understanding of the kinds of medical care that most patients need. The insurance companies choices may mean that the test, drug, or service you provided isn't covered by the policy.</p>
    <ul style="padding-left:5px"><li>• It's better to know what the insurance company will pay for before you provide a service, test or fill a prescription. Some kinds of care may have to be approved by the insurance company before you can provide them.</li></ul>
    <p>When a test or treatment isn't covered the insurance company won't pay the bill. This is called "denying the claim." If your insurance company denies your claim, you have the right to appeal (challenge) the decision.</p>
  </div>
  <svg class="corner" viewBox="0 0 28 28"><path d="M28 0V28H0z" fill="#c9ad7d"/><path d="M28 9V28H9z" fill="#8d6116"/></svg>
</section>

<section class="page violet" style="left:283px;top:603px">
  <svg class="wires" viewBox="0 0 222 282" fill="none" stroke="#4a2a8f" stroke-width=".6">
    <path d="M108 51V96M51 96H168"/><path d="M51 96V106" marker-end="url(#ah-violet)"/><path d="M168 96V106" marker-end="url(#ah-violet)"/>
  </svg>
  <div class="banner" style="top:22px;height:29px">Claim Denied as Global Inclusive</div>
  <div class="box" style="left:17px;top:107px;width:68px;height:59px">Claim denied and has been sent back to process</div>
  <div class="box" style="left:133px;top:107px;width:69px;height:59px">Claim is global inclusive to claim resolved accounts</div>
  <svg class="corner" viewBox="0 0 28 28"><path d="M28 0V28H0z" fill="#a594c8"/><path d="M28 9V28H9z" fill="#4a2a8f"/></svg>
</section>

<section class="page violet" style="left:508px;top:603px">
  <div class="heading" style="top:23px">Global Surgical Package</div>
  <div class="rule" style="top:33px"></div>
  <div class="copy" style="left:50px;top:52px;width:130px">
    <ul>
      <li>• The global surgical package is a single payment for all care associated with a surgical procedure. Within 10 days.</li>
      <li>• Other names for the Global Surgical Package include: Postoperative Period, Global Period, Global Services, Surgical Period, Global package and Global Surgery.</li>
      <li>• Care of a patient during the global surgical period is not restricted to any specific location. A patient may be treated by the surgeon (or other provider of the same medical group and specialty) in just about any location including inpatient hospital, outpatient hospital, ambulatory surgical center, nursing home, surgeon's office, emergency room, urgent care, and even the intensive care unit of a hospital.</li>
    </ul>
  </div>
  <div class="heading" style="top:145px;left:50px;width:130px;font-size:5.8px">No Charge Services</div>
  <div class="rule" style="top:153px;left:70px;width:90px;height:1px"></div>
  <div class="copy" style="left:52px;top:166px;width:128px">
    <p>There are several services that are not charged services as they are associated with another service.</p>
    <ul style="padding-left:6px"><li>• Suture removal placed at this office</li><li>• Routine I&amp;D follow up</li><li>• Sprain follow up</li><li>• Corneal abrasion follow up</li></ul>
  </div>
  <svg class="corner" viewBox="0 0 28 28"><path d="M28 0V28H0z" fill="#a594c8"/><path d="M28 9V28H9z" fill="#4a2a8f"/></svg>
</section>

<section class="page blue" style="left:733px;top:603px">
  <svg class="wires" viewBox="0 0 222 282" fill="none" stroke="#0c56a6" stroke-width=".6">
    <path d="M108 53V98M64 98H155"/><path d="M64 98V108" marker-end="url(#ah-blue)"/><path d="M155 98V108" marker-end="url(#ah-blue)"/>
    <path d="M64 143V149M155 143V149M64 149H155"/><path d="M97 149V154" marker-end="url(#ah-blue)"/><path d="M117 149V154" marker-end="url(#ah-blue)"/>
    <path d="M107 178V195" marker-end="url(#ah-blue)"/>
    <path d="M47 126H38V206H92" marker-end="url(#ah-blue)"/>
    <path d="M176 126H188V206H124" marker-end="url(#ah-blue)"/>
  </svg>
  <div class="banner" style="top:22px;height:31px">Additional Information Requested</div>
  <div class="box" style="left:47px;top:109px;width:35px;height:34px">Additional information requested from provider.<em>See Attachment</em></div>
  <div class="box" style="left:135px;top:109px;width:41px;height:34px">Additional information requested from patient.<em>See Attachment</em></div>
  <div class="box" style="left:91px;top:155px;width:32px;height:23px">Applied to patient responsibility</div>
  <div class="box" style="left:93px;top:196px;width:30px;height:21px">Claim paid</div>
  <div class="side" style="left:18px;top:114px;width:28px;text-align:right">* Primary EOB<br><br>* Medical Records</div>
  <div class="side" style="left:180px;top:114px;width:36px">* COB Update<br><br>* Third party liability form</div>
  <svg class="corner" viewBox="0 0 28 28"><path d="M28 0V28H0z" fill="#86aad3"/><path d="M28 9V28H9z" fill="#0c56a6"/></svg>
</section>

<!-- Row 4 -->
<section class="page blue" style="left:58px;top:892px">
  <div class="heading" style="top:14px;font-size:6.2px;line-height:1.35">Claim Has Been Denied Requesting<br>Additional Information From the Patient</div>
  <div class="rule" style="top:33px"></div>
  <div class="copy" style="left:40px;top:48px;width:140px">
    <p class="sub" style="font-size:3.6px">Carrier Questions for note:</p>
    <ul>
      <li>• Who did you speak to?</li><li>• What is the phone number?</li><li>• What is the claim number?</li><li>• When did the claim deny?</li>
      <li>• What has been requested from the patient? When was the patient last contacted?</li>
      <li>• How can the patient respond to your request? Fax? Phone? Mail?</li>
      <li>• Claim denied for Third Party Liability Forms/ Accident Details (TPL) that the service performed was due to an injury. If services was not for an injury have the rep send claim back to process.</li>
      <li>• Claim denied for Coordination of Benefits update (COB) Ask what other carrier they are showing on file. ID number ect...</li>
      <li>• Claim denied for missing or incomplete policy information. What is missing? Have other claims paid? How?</li>
      <li>• Follow up on the account. If patient has not responded put balance to the patient.</li>
    </ul>
  </div>
  <svg class="corner" viewBox="0 0 28 28"><path d="M28 0V28H0z" fill="#86aad3"/><path d="M28 9V28H9z" fill="#0c56a6"/></svg>
</section>

<section class="page blue" style="left:283px;top:892px">
  <div class="heading" style="top:21px">Pending Information From Provider</div>
  <div class="rule" style="top:31px"></div>
  <div class="copy" style="left:38px;top:46px;width:150px">
    <p class="sub">PRIMARY EOB REQUIRED</p>
    <p><b>Account note will include:</b><br>*How information was obtained<br>*Name of representative<br>*Phone number<br>*Claim number<br>* Denial date<br>*Name of primary carrier on file</p>
    <p>1. Claim has previously been billed to the primary carrier: Print EOB and rebill with claim.</p>
    <p>2. Claim was not sent to primary carrier: Send claim to that carrier.</p>
    <p>3. Claim was not billed to primary carrier as the patient did not inform clinic of other insurance coverage. Representative supplies primary carrier on file: Call will be made to the carrier to verify: ID number, group number, effective dates, claim address, timely filing deadline. Insurance information will be added to patient information and claim will be sent.</p>
    <p>4. Claim was not billed to the primary carrier, representative did not give other health insurance information patient will be sent Coordination of Benefits letter.</p>
  </div>
  <svg class="corner" viewBox="0 0 28 28"><path d="M28 0V28H0z" fill="#86aad3"/><path d="M28 9V28H9z" fill="#0c56a6"/></svg>
</section>

<section class="page orange" style="left:508px;top:892px">
  <svg class="wires" viewBox="0 0 222 282" fill="none" stroke="#f38a1f" stroke-width=".6">
    <path d="M108 52V80M50 80H166"/><path d="M50 80V93" marker-end="url(#ah-orange)"/><path d="M166 80V93" marker-end="url(#ah-orange)"/>
    <path d="M108 80V147" marker-end="url(#ah-orange)"/><path d="M108 202V230" marker-end="url(#ah-orange)"/>
  </svg>
  <div class="banner" style="top:20px;height:32px">Claim/Appeal Denied for Past Timely Filing.</div>
  <div class="box" style="left:30px;top:94px;width:40px;height:51px">Claim is not past timely filing and rep. sends claim back to process.</div>
  <div class="box" style="left:146px;top:94px;width:40px;height:51px">Account is past filing deadline</div>
  <div class="box" style="left:88px;top:148px;width:42px;height:54px">Rep. will not send claim back to process, but you find proof that claim was not past filing deadline.</div>
  <div class="box" style="left:88px;top:231px;width:40px;height:23px">Timely filing appeal sent.</div>
  <svg class="corner" viewBox="0 0 28 28"><path d="M28 0V28H0z" fill="#f9c38b"/><path d="M28 9V28H9z" fill="#f38a1f"/></svg>
</section>

<section class="page orange" style="left:733px;top:892px">
  <div class="heading" style="top:22px">Past Timely Filing</div>
  <div class="rule" style="top:32px"></div>
  <div class="copy" style="left:60px;top:52px;width:130px">
    <p>* Carrier filing Limits:<br>&nbsp;&nbsp;Senior Care Plan: Claim: 60 days appeals: 180 days<br>&nbsp;&nbsp;Apex Health: Claim: 120 days appeals: 180 days<br>&nbsp;&nbsp;Shield Mutual: Claim: 90 days<br>&nbsp;&nbsp;Cedar Health: Claim: 90 days appeals: 180 days<br>&nbsp;&nbsp;Crestview Care: Claim: 180 days<br>&nbsp;&nbsp;Harbor Health: Claim 90 days appeals: 18 months<br>&nbsp;&nbsp;State Aid Plan: 365 days<br>&nbsp;&nbsp;Unity Health: claim 90 days<br>&nbsp;&nbsp;Tri-Service Plan: 365 days</p>
    <p>Account notes will include:<br>&nbsp;&nbsp;* Claim number<br>&nbsp;&nbsp;* Denial date<br>&nbsp;&nbsp;* Date the claim/appeal was received.<br>&nbsp;&nbsp;* Filing deadline<br>&nbsp;&nbsp;* Date original (first) claim or appeal was received?<br>&nbsp;&nbsp;* Appeal address<br>&nbsp;&nbsp;* Appeal timely filing</p>
    <p>&nbsp;&nbsp;* Claim is not past timely filing have the representative send the claim back to process.<br>&nbsp;&nbsp;* If rep. will not send claim back to process. Send appeal.</p>
  </div>
  <svg class="corner" viewBox="0 0 28 28"><path d="M28 0V28H0z" fill="#f9c38b"/><path d="M28 9V28H9z" fill="#f38a1f"/></svg>
</section>
</body>
</html>
```